Form Crafters Business Card

Professional cosmetic surgery company, based in very exclusive area in London. High profiled clientele. Brand is very artistic, modern, state-of-the-art, safe. The best in the business. Celebrity clientele.

Form Crafter’s of London is a brand serving a discriminating and exclusive clientele who value personal service that is both intimate and high end. Our clients choose Form Crafters because of the relationships we share with all of our customers. The clients of Form Crafters have an equal partnership between customers, and very experienced, highly qualified medical professionals. This together provides you with a professional service that keeps you looking good and feeling good. It is a relationship based on honesty, compassion, loyalty and respect.
Form Crafter’s have provided services for internationally recognised celebrities, and other high profiled individuals.

The cards are used for networking at private, exclusive events with VIPs.

Target Market(s)

Professionals
Rich people

Industry/Entity Type

Professional Service

Contact Information for Business Card

Need double sided business card design for 4 people. Back of the business card needs to have contrast background to the front with butterfly watermark with services provided:
Hair Restoration surgery
Hair Loss treatments
Breast surgery
Rhinoplasty
Zelix Liposuction
Fat Grafting
Lumex & Fillers

Front of the business card needs to be a nice satin black.
with following information:
Talvan Desoruthy - name
Chief Executive - Job title

www.formcrafters-example.co.uk
talvan@formcrafters-example.co.uk
Phone: +44 (0)207 146 5327
Mobile: +44 (0)7491 825 436

The London Calder Infirmary
14 Pellmont Street | London | W1K 3TR
Off Dunmore Lane

All business cards have the same address, phone, website as Talvan's details.
Same details on the back of the business card as well.
The other cards have different name, job title, email, mobile number

Kerem Lutz - Name
Partner - Job Title
Former England International Cricketer - please include below job title

email: kerem@formcrafters-example.co.uk
mobile: +44(0)7862 514208

Dr Stellan Vastrel - Name
Plastic Surgeon - Job Title
drvastrel@formcrafters-example.co.uk
No mobile number

Dr Jon Torvick FRCS (please put FRCS in small font) - Name
Hair Restoration Surgeon - Job Title
drtorvick@formcrafters-example.co.uk
No mobile number

Colors
cedeec
85abd2
0655a3

Requirements
Must have
• The logo needs to be in a metallic finish
• Text needs to be striking
• nice background
• butterfly watermark on the back

```html
<!DOCTYPE html>
<html lang="en">
<head>
<meta charset="utf-8">
<title>Form Crafters Business Card</title>
<link rel="stylesheet" href="https://fonts.googleapis.com/css2?family=Open+Sans:wght@400;600;700;800&display=swap">
<style>
  :root {
    --page-bg: #e9e6e1;
    --orange-light: #f7a51e;
    --orange-deep: #f0561a;
    --orange-accent: #f26a1b;
    --service-text: #c65a1e;
    --tick-blue: #1f73c9;
    --title-blue: #2f7fd0;
    --card-black: #050505;
    --white: #ffffff;
    --gold: #f3a51f;
  }
  * { box-sizing: border-box; margin: 0; padding: 0; }
  html, body { width: 1200px; height: 900px; overflow: hidden; }
  body {
    background: var(--page-bg);
    font-family: "Open Sans", Arial, sans-serif;
    position: relative;
  }
  .card {
    position: absolute;
    left: 250px;
    width: 700px;
    height: 400px;
    border-radius: 4px;
    box-shadow: 0 8px 24px rgba(0,0,0,0.25);
    overflow: hidden;
  }
  /* Back side */
  .card-back {
    top: 25px;
    background: linear-gradient(160deg, var(--orange-light) 0%, var(--orange-deep) 100%);
  }
  .service-list {
    position: absolute;
    left: 46px;
    top: 72px;
    list-style: none;
  }
  .service-list li {
    display: flex;
    align-items: center;
    gap: 12px;
    font-weight: 800;
    font-size: 19px;
    letter-spacing: 0.6px;
    line-height: 32px;
    color: var(--service-text);
    text-transform: uppercase;
  }
  .service-list svg { width: 22px; height: 22px; flex: none; }
  .watermark-name {
    position: absolute;
    right: 48px;
    top: 150px;
    font-weight: 700;
    font-size: 40px;
    color: rgba(255, 200, 80, 0.55);
  }
  /* Front side */
  .card-front {
    top: 465px;
    background: radial-gradient(ellipse at 50% 20%, #1a1a1a 0%, var(--card-black) 70%);
    color: var(--white);
  }
  .brand {
    position: absolute;
    top: 22px;
    left: 0; right: 0;
    text-align: center;
  }
  .brand-name {
    font-weight: 600;
    font-size: 42px;
    line-height: 52px;
    color: var(--gold);
    letter-spacing: 1px;
  }
  .brand-tagline {
    display: block;
    font-size: 11px;
    letter-spacing: 1.5px;
    color: var(--gold);
    text-transform: uppercase;
  }
  .address {
    position: absolute;
    left: 40px;
    right: 40px;
    top: 108px;
    font-size: 13px;
    font-weight: 600;
    line-height: 20px;
    white-space: nowrap;
    text-align: center;
  }
  .rule {
    position: absolute;
    left: 40px;
    right: 40px;
    height: 2px;
    background: var(--orange-accent);
  }
  .rule-top { top: 142px; }
  .rule-mid { top: 238px; }
  .company-contact {
    position: absolute;
    right: 40px;
    top: 160px;
    text-align: right;
    font-size: 15px;
    font-weight: 600;
    line-height: 30px;
  }
  .contact-line { display: flex; align-items: center; gap: 10px; }
  .company-contact .contact-line { justify-content: flex-end; }
  .contact-line svg { width: 18px; height: 18px; flex: none; }
  .person {
    position: absolute;
    left: 40px;
    top: 160px;
  }
  .person-name {
    font-weight: 800;
    font-size: 24px;
    line-height: 32px;
    color: var(--orange-accent);
    text-transform: uppercase;
    letter-spacing: 0.5px;
  }
  .person-title {
    font-weight: 700;
    font-size: 18px;
    line-height: 26px;
    color: var(--title-blue);
  }
  .person-contact {
    position: absolute;
    left: 40px;
    top: 262px;
    font-size: 17px;
    font-weight: 600;
    line-height: 34px;
  }
</style>
</head>
<body>

<section class="card card-back" aria-label="Card back">
  <ul class="service-list">
    <li><svg viewBox="0 0 24 24"><path d="M3 12l6 6L21 5" fill="none" stroke="var(--tick-blue)" stroke-width="4" stroke-linecap="round" stroke-linejoin="round"/></svg>Hair Restoration Surgery</li>
    <li><svg viewBox="0 0 24 24"><path d="M3 12l6 6L21 5" fill="none" stroke="var(--tick-blue)" stroke-width="4" stroke-linecap="round" stroke-linejoin="round"/></svg>Hair Loss Treatments</li>
    <li><svg viewBox="0 0 24 24"><path d="M3 12l6 6L21 5" fill="none" stroke="var(--tick-blue)" stroke-width="4" stroke-linecap="round" stroke-linejoin="round"/></svg>Breast Surgery</li>
    <li><svg viewBox="0 0 24 24"><path d="M3 12l6 6L21 5" fill="none" stroke="var(--tick-blue)" stroke-width="4" stroke-linecap="round" stroke-linejoin="round"/></svg>Rhinoplasty</li>
    <li><svg viewBox="0 0 24 24"><path d="M3 12l6 6L21 5" fill="none" stroke="var(--tick-blue)" stroke-width="4" stroke-linecap="round" stroke-linejoin="round"/></svg>Zelix Liposuction</li>
    <li><svg viewBox="0 0 24 24"><path d="M3 12l6 6L21 5" fill="none" stroke="var(--tick-blue)" stroke-width="4" stroke-linecap="round" stroke-linejoin="round"/></svg>Fat Grafting</li>
    <li><svg viewBox="0 0 24 24"><path d="M3 12l6 6L21 5" fill="none" stroke="var(--tick-blue)" stroke-width="4" stroke-linecap="round" stroke-linejoin="round"/></svg>Lumex</li>
    <li><svg viewBox="0 0 24 24"><path d="M3 12l6 6L21 5" fill="none" stroke="var(--tick-blue)" stroke-width="4" stroke-linecap="round" stroke-linejoin="round"/></svg>Fillers</li>
  </ul>
  <div class="watermark-name" aria-hidden="true">Form Crafters</div>
</section>

<section class="card card-front" aria-label="Card front">
  <div class="brand">
    <div class="brand-name">Form Crafters</div>
    <span class="brand-tagline">Refined Care, Lasting Confidence</span>
  </div>
  <p class="address">The London Calder Infirmary 14 Pellmont Street | London | W1K 3TR Off Dunmore Lane</p>
  <div class="rule rule-top"></div>
  <div class="person">
    <div class="person-name">Talvan Desoruthy</div>
    <div class="person-title">Chief Executive</div>
  </div>
  <div class="company-contact">
    <div class="contact-line">+44 (0)207 146 5327
      <svg viewBox="0 0 24 24"><path d="M6 3l4 4-2 3c1 3 3 5 6 6l3-2 4 4-3 3C10 20 4 14 3 6z" fill="none" stroke="var(--orange-accent)" stroke-width="2" stroke-linejoin="round"/></svg>
    </div>
    <div class="contact-line">www.formcrafters-example.co.uk
      <svg viewBox="0 0 24 24"><rect x="3" y="4" width="18" height="12" fill="none" stroke="var(--orange-accent)" stroke-width="2"/><path d="M9 20h6M12 16v4" stroke="var(--orange-accent)" stroke-width="2"/></svg>
    </div>
  </div>
  <div class="rule rule-mid"></div>
  <div class="person-contact">
    <div class="contact-line">
      <svg viewBox="0 0 24 24"><rect x="6" y="2" width="12" height="20" rx="2" fill="none" stroke="var(--orange-accent)" stroke-width="2"/></svg>
      +44 (0)7491 825 436
    </div>
    <div class="contact-line">
      <svg viewBox="0 0 24 24"><rect x="2" y="5" width="20" height="14" fill="var(--orange-accent)"/><path d="M2 5l10 8 10-8" fill="none" stroke="var(--card-black)" stroke-width="1.5"/></svg>
      talvan@formcrafters-example.co.uk
    </div>
  </div>
</section>

</body>
</html>
```